New business card design needed for Diesel Fitting (Mechanical) Company

We need a new business card for our company called "Gumtree Engine Works" that showcases our logo and business details.
Target Market(s)
Owners of all makes and models of vehicles, trucks, plant and machinery.
Industry/Entity Type
Mechanical
Contact Information for Business Card
The business card details need to include the following: Owners/Directors: Doug & Marisol Brent-Coyle ABN: 41 917 302 846 Address: 317 Wattlebrook Street CHARTERS TOWERS QLD 4820 Postal Address: PO Box 5791 CHARTERS TOWERS QLD 4820 Website: www.gewservice.com.au Phone: 4712 9083 Mobile: 0438 175 906 Emails: sales@gewservice.com.au; admin@gewservice.com.au; accounts@gewservice.com.au; parts@gewservice.com.au; office@gewservice.com.au, reception@gewservice.com.au
Look and feel

```html
<!DOCTYPE html>
<html lang="en">
<head>
<meta charset="utf-8">
<title>Gumtree Engine Works – Business Card</title>
<link href="https://fonts.googleapis.com/css2?family=Poppins:wght@300;400;500;600;700&display=swap" rel="stylesheet">
<style>
  :root {
    --page: #d9d9d9;
    --card: #1d1d1e;
    --orange: #f47a20;
    --red: #e3242b;
    --yellow: #fcc012;
    --grey: #b8b8b8;
    --rule: #4a4a4a;
    --band-text: #2a0b0b;
  }
  * { box-sizing: border-box; margin: 0; padding: 0; }
  html, body { width: 1200px; height: 900px; overflow: hidden; }
  body {
    background: var(--page);
    font-family: "Poppins", sans-serif;
    position: relative;
  }
  .card {
    position: absolute;
    left: 250px;
    width: 700px;
    height: 400px;
    background: var(--card);
    border-radius: 4px;
    overflow: hidden;
    box-shadow: 0 10px 30px rgba(0,0,0,.25);
    color: var(--grey);
  }
  .card--front { top: 35px; }
  .card--back { top: 465px; }

  .stripes { position: absolute; inset: 0; }

  .owner { position: absolute; left: 42px; top: 34px; }
  .owner__name { color: var(--orange); font-weight: 700; font-size: 20px; line-height: 1.2; }
  .owner__role { color: var(--red); font-size: 13px; font-weight: 400; margin-top: 2px; }
  .owner__abn { font-size: 13px; font-weight: 300; }

  .contact-row { display: flex; align-items: center; gap: 8px; font-size: 14px; font-weight: 400; line-height: 1.7; }
  .icon { width: 16px; height: 16px; flex: none; }
  .phones { position: absolute; left: 42px; top: 112px; }

  .emails { position: absolute; left: 42px; top: 168px; display: flex; gap: 8px; }
  .emails ul { list-style: none; font-size: 13px; font-weight: 300; line-height: 1.5; }

  .brand { position: absolute; right: 44px; top: 158px; display: flex; align-items: center; gap: 10px; }
  .brand__dot { width: 14px; height: 14px; border-radius: 50%; background: var(--orange); flex: none; }
  .brand__name { color: var(--orange); font-weight: 600; font-size: 24px; letter-spacing: .2px; }

  .address { position: absolute; left: 400px; top: 222px; width: 256px; font-size: 12.5px; font-weight: 400; line-height: 1.45; }
  .address__block { display: flex; gap: 8px; }
  .address__block + .address__block { margin-top: 10px; padding-top: 10px; border-top: 1px solid var(--rule); }
  .address__label { color: var(--orange); font-weight: 500; }

  .web { position: absolute; right: 40px; top: 356px; display: flex; align-items: center; gap: 8px; color: var(--band-text); font-weight: 600; font-size: 14px; letter-spacing: 1px; }

  .back__brand { position: absolute; left: 0; right: 0; top: 150px; display: flex; justify-content: center; align-items: center; gap: 12px; }
  .back__brand .brand__dot { width: 20px; height: 20px; }
  .back__brand .brand__name { font-size: 38px; }
  .back__web { position: absolute; left: 0; right: 0; top: 222px; text-align: center; font-size: 15px; letter-spacing: 2px; font-weight: 400; }
</style>
</head>
<body>

<section class="card card--front">
  <svg class="stripes" width="700" height="400" viewBox="0 0 700 400" aria-hidden="true">
    <polygon points="0,304 340,304 350,316 0,316" fill="var(--yellow)"/>
    <polygon points="0,322 330,322 352,346 700,346 700,380 0,380" fill="var(--red)"/>
  </svg>

  <div class="owner">
    <p class="owner__name">Doug &amp; Marisol Brent-Coyle</p>
    <p class="owner__role">Owners/Directors</p>
    <p class="owner__abn">ABN: 41 917 302 846</p>
  </div>

  <div class="phones">
    <p class="contact-row">
      <svg class="icon" viewBox="0 0 16 16"><circle cx="8" cy="8" r="7" fill="none" stroke="var(--orange)" stroke-width="1.4"/><path d="M5.5 4.5l1.3 1.6-.8.9c.5 1 1.2 1.7 2.1 2.1l.9-.8 1.6 1.3-.7 1.2c-2.5-.4-4.6-2.5-5-5z" fill="var(--orange)"/></svg>
      4712 9083
    </p>
    <p class="contact-row">
      <svg class="icon" viewBox="0 0 16 16"><circle cx="8" cy="8" r="7" fill="none" stroke="var(--orange)" stroke-width="1.4"/><rect x="5.6" y="4" width="4.8" height="8" rx="1" fill="none" stroke="var(--orange)" stroke-width="1.2"/></svg>
      0438 175 906
    </p>
  </div>

  <div class="emails">
    <svg class="icon" viewBox="0 0 16 16"><circle cx="8" cy="8" r="7" fill="none" stroke="var(--orange)" stroke-width="1.4"/><rect x="4.5" y="5.5" width="7" height="5" fill="none" stroke="var(--orange)" stroke-width="1.1"/><path d="M4.5 5.5L8 8.4l3.5-2.9" fill="none" stroke="var(--orange)" stroke-width="1.1"/></svg>
    <ul>
      <li>sales@gewservice.com.au</li>
      <li>admin@gewservice.com.au</li>
      <li>accounts@gewservice.com.au</li>
      <li>parts@gewservice.com.au</li>
      <li>office@gewservice.com.au</li>
      <li>reception@gewservice.com.au</li>
    </ul>
  </div>

  <div class="brand">
    <span class="brand__dot"></span>
    <span class="brand__name">Gumtree Engine Works</span>
  </div>

  <div class="address">
    <div class="address__block">
      <svg class="icon" viewBox="0 0 16 16"><circle cx="8" cy="8" r="7" fill="none" stroke="var(--orange)" stroke-width="1.4"/><path d="M8 12.2s-2.8-3-2.8-5a2.8 2.8 0 015.6 0c0 2-2.8 5-2.8 5z" fill="none" stroke="var(--orange)" stroke-width="1.1"/><circle cx="8" cy="7.1" r="1" fill="var(--orange)"/></svg>
      <p>317 Wattlebrook Street<br>CHARTERS TOWERS QLD 4820</p>
    </div>
    <div class="address__block">
      <svg class="icon" viewBox="0 0 16 16"><circle cx="8" cy="8" r="7" fill="none" stroke="var(--orange)" stroke-width="1.4"/><path d="M8 12.2s-2.8-3-2.8-5a2.8 2.8 0 015.6 0c0 2-2.8 5-2.8 5z" fill="none" stroke="var(--orange)" stroke-width="1.1"/><circle cx="8" cy="7.1" r="1" fill="var(--orange)"/></svg>
      <p><span class="address__label">Postal Address:</span><br>PO Box 5791<br>CHARTERS TOWERS QLD 4820</p>
    </div>
  </div>

  <p class="web">
    <svg class="icon" viewBox="0 0 16 16"><circle cx="8" cy="8" r="6.5" fill="none" stroke="var(--band-text)" stroke-width="1.3"/><ellipse cx="8" cy="8" rx="2.8" ry="6.5" fill="none" stroke="var(--band-text)" stroke-width="1.1"/><path d="M1.5 8h13M2.6 4.8h10.8M2.6 11.2h10.8" stroke="var(--band-text)" stroke-width="1"/></svg>
    WWW.GEWSERVICE.COM.AU
  </p>
</section>

<section class="card card--back">
  <div class="back__brand">
    <span class="brand__dot"></span>
    <span class="brand__name">Gumtree Engine Works</span>
  </div>
  <p class="back__web">WWW.GEWSERVICE.COM.AU</p>
</section>

</body>
</html>
```